lumineaux project business card, interior design and decoration firm

I'm a young woman and I've just created my interior design consulting firm. I'm very inspired by brasilian design, italian design, argentinian spirit, I like pure forms, chic colors (blue specially) and raw stuffs (wood, glass,
I work with wines properties, boats and yachts dealers, private people. Elegant but inspired
It's very important to dedicate one side to this card to the name Lumineaux. I would like my name on the other side (Claire-Anne Vostel), my mail cavostel@mailrivo.com, my number + 33 6 12 58 39 91

Target Market(s)

middle and upper class, young people,

Contact Information for Business Card

Font styles to use
Sans Serif

Colors
0255a3
85abd2
000000
fdfdfd
86cfc6
fdf0f6
00a990
f04a50

Requirements
Must have
• The name Lumineaux, my name my number and mail one or two colors max, one logo if it's possible. AND uder The name Lumineaux "Cabinet de conseil en aménagement intérieur"

```html
<!DOCTYPE html>
<html lang="en">
<head>
<meta charset="utf-8">
<title>Lumineaux – business card</title>
<link rel="stylesheet" href="https://fonts.googleapis.com/css2?family=Cinzel:wght@500;600&family=Roboto+Condensed:ital,wght@0,400;1,400;1,700&display=swap">
<style>
  :root {
    --page-bg: #3b3b3b;
    --brand-blue: #1645a0;
    --wood-dark: #2a160c;
    --wood-mid: #4a2814;
    --gold: #e9d39a;
    --ink-white: #fdfdfd;
    --name-blue: #1b3f8f;
    --teal: #1a9aa6;
    --ink-black: #111111;
    --panel-grey: #d3d3da;
  }
  html, body {
    margin: 0;
    width: 1200px;
    height: 1200px;
    overflow: hidden;
    background: var(--page-bg);
  }
  .canvas {
    position: relative;
    width: 1200px;
    height: 1200px;
  }
  .card {
    position: absolute;
    left: 254px;
    width: 691px;
    height: 414px;
    display: block;
  }
  .card--front { top: 123px; }
  .card--back { top: 616px; }
  .wordmark {
    font-family: "Cinzel", serif;
    font-weight: 500;
    fill: var(--gold);
  }
  .tagline {
    font-family: "Roboto Condensed", sans-serif;
    font-style: italic;
    font-weight: 400;
  }
  .tagline--light { fill: var(--ink-white); }
  .tagline--teal { fill: var(--teal); }
  .holder-name {
    font-family: "Cinzel", serif;
    font-weight: 600;
    fill: var(--name-blue);
  }
  .contact {
    font-family: "Roboto Condensed", sans-serif;
    fill: var(--ink-black);
  }
  .contact--phone { font-style: italic; font-weight: 700; }
  .contact--mail { font-weight: 400; }
  .contact-icon { fill: var(--teal); }
  .contact-at {
    font-family: "Roboto Condensed", sans-serif;
    font-style: italic;
    font-weight: 700;
    fill: var(--teal);
  }
</style>
</head>
<body>
<div class="canvas">

  <!-- Front: brand side -->
  <svg class="card card--front" viewBox="0 0 864 518" xmlns="http://www.w3.org/2000/svg">
    <defs>
      <linearGradient id="woodGrain" x1="0" y1="0" x2="1" y2="1">
        <stop offset="0" stop-color="#3d2112"/>
        <stop offset="0.5" stop-color="#2a160c"/>
        <stop offset="1" stop-color="#3a1f10"/>
      </linearGradient>
      <linearGradient id="bouquetTones" x1="0" y1="0" x2="1" y2="1">
        <stop offset="0" stop-color="#6b4a34"/>
        <stop offset="0.45" stop-color="#c8507a"/>
        <stop offset="1" stop-color="#3f6a34"/>
      </linearGradient>
      <linearGradient id="roseTones" x1="0" y1="0" x2="1" y2="0">
        <stop offset="0" stop-color="#cfd0d6"/>
        <stop offset="0.55" stop-color="#e8b4bd"/>
        <stop offset="1" stop-color="#4f7a3c"/>
      </linearGradient>
      <linearGradient id="loungeTones" x1="0" y1="0" x2="1" y2="1">
        <stop offset="0" stop-color="#e8e0cf"/>
        <stop offset="1" stop-color="#7a3f22"/>
      </linearGradient>
      <linearGradient id="mirrorTones" x1="0" y1="0" x2="1" y2="1">
        <stop offset="0" stop-color="#1e2430"/>
        <stop offset="0.6" stop-color="#141414"/>
        <stop offset="1" stop-color="#2a1d14"/>
      </linearGradient>
    </defs>
    <rect class="card-base" width="864" height="518" fill="var(--brand-blue)"/>
    <polygon role="img" aria-label="Dark mantelpiece with a gilded mirror and books" points="613,268 864,166 864,518 520,518" fill="url(#mirrorTones)"/>
    <polygon role="img" aria-label="Glass table with a vase of dried hydrangeas" points="0,306 173,376 250,518 0,518" fill="url(#loungeTones)"/>
    <polygon role="img" aria-label="Pink camellias and glassware on a white table" points="173,376 690,240 523,518 250,518" fill="url(#roseTones)"/>
    <polygon role="img" aria-label="Bouquet of orchids and pink gerberas on a wooden table" points="576,0 700,0 864,168 613,268" fill="url(#bouquetTones)"/>
    <polygon role="img" aria-label="Dark walnut wood grain" points="114,0 576,0 613,268 173,376 0,201" fill="url(#woodGrain)"/>
    <text class="wordmark" x="98" y="208" font-size="76" textLength="450" lengthAdjust="spacingAndGlyphs">LUMINEAUX</text>
    <text class="tagline tagline--light" x="551" y="251" font-size="28" text-anchor="end">interior design consulting firm</text>
  </svg>

  <!-- Back: holder side -->
  <svg class="card card--back" viewBox="0 0 864 518" xmlns="http://www.w3.org/2000/svg">
    <defs>
      <linearGradient id="bouquetTonesB" x1="0" y1="0" x2="1" y2="1">
        <stop offset="0" stop-color="#6b4a34"/>
        <stop offset="0.45" stop-color="#c8507a"/>
        <stop offset="1" stop-color="#3f6a34"/>
      </linearGradient>
      <linearGradient id="roseTonesB" x1="0" y1="0" x2="1" y2="0">
        <stop offset="0" stop-color="#cfd0d6"/>
        <stop offset="0.55" stop-color="#e8b4bd"/>
        <stop offset="1" stop-color="#4f7a3c"/>
      </linearGradient>
      <linearGradient id="loungeTonesB" x1="0" y1="0" x2="1" y2="1">
        <stop offset="0" stop-color="#e8e0cf"/>
        <stop offset="1" stop-color="#7a3f22"/>
      </linearGradient>
      <linearGradient id="mirrorTonesB" x1="0" y1="0" x2="1" y2="1">
        <stop offset="0" stop-color="#1e2430"/>
        <stop offset="0.6" stop-color="#141414"/>
        <stop offset="1" stop-color="#2a1d14"/>
      </linearGradient>
    </defs>
    <rect class="card-base" width="864" height="518" fill="var(--brand-blue)"/>
    <polygon role="img" aria-label="Dark mantelpiece with a gilded mirror and books" points="613,268 864,166 864,518 520,518" fill="url(#mirrorTonesB)"/>
    <polygon role="img" aria-label="Glass table with a vase of dried hydrangeas" points="0,306 173,376 250,518 0,518" fill="url(#loungeTonesB)"/>
    <polygon role="img" aria-label="Pink camellias and glassware on a white table" points="173,376 690,240 523,518 250,518" fill="url(#roseTonesB)"/>
    <polygon role="img" aria-label="Bouquet of orchids and pink gerberas on a wooden table" points="576,0 700,0 864,168 613,268" fill="url(#bouquetTonesB)"/>
    <polygon class="panel-grey" points="470,0 576,0 613,268 500,300 575,150" fill="var(--panel-grey)"/>
    <polygon class="panel-white" points="114,0 470,0 575,150 500,300 173,376 0,201" fill="var(--ink-white)"/>
    <text class="holder-name" x="81" y="150" font-size="46" textLength="432" lengthAdjust="spacingAndGlyphs">CLAIRE-ANNE VOSTEL</text>
    <text class="tagline tagline--teal" x="506" y="184" font-size="27" text-anchor="end">interior design consulting firm</text>
    <path class="contact-icon" d="M249 220c-3 2-3 6-1 12s6 11 11 13c3 1 5 0 6-2l-4-5-3 1c-3-2-5-5-6-9l2-2-2-7z"/>
    <text class="contact contact--phone" x="283" y="242" font-size="27">+33 6 12 58 39 91</text>
    <text class="contact-at" x="247" y="286" font-size="26">@</text>
    <text class="contact contact--mail" x="283" y="280" font-size="22">cavostel@mailrivo.com</text>
  </svg>

</div>
</body>
</html>
```